Mabel's Fitness Business Cards

I would like my business cards to look expensive and sophisticated using my logo and the information below.

FRONT
Mabel’s Fitness logo

Tag line Become your happiest, healthiest and strongest self

Mabel Quint Harlow
Personal Trainer

e. mabel@mabelsfitstudio.example

t. 0781530462

w. www.mabelsfitstudio.example

```html
<!DOCTYPE html>
<html lang="en">
<head>
<meta charset="utf-8">
<title>Mabel’s Fitness Business Cards</title>
<link rel="stylesheet" href="https://fonts.googleapis.com/css2?family=Roboto:wght@300;400&display=swap">
<style>
  :root {
    --backdrop: #d4d5d7;
    --card-white: #ffffff;
    --teal: #5cb1b6;
    --teal-deep: #2f9a9c;
    --teal-light: #a9d4d6;
    --taupe: #998c8c;
    --text-light: #ffffff;
  }
  * { margin: 0; padding: 0; box-sizing: border-box; }
  html, body {
    width: 1200px;
    height: 1200px;
    overflow: hidden;
    background: var(--backdrop);
    font-family: "Roboto", Arial, sans-serif;
    font-weight: 300;
  }
  .card {
    position: absolute;
    left: 192px;
    width: 816px;
    height: 528px;
    background: var(--card-white);
    overflow: hidden;
  }
  .card--front { top: 48px; }
  .card--back { top: 622px; }

  .business-name {
    position: absolute;
    left: 0;
    right: 0;
    top: 0;
    height: 442px;
    display: flex;
    align-items: center;
    justify-content: center;
    color: var(--teal);
    font-weight: 300;
    font-size: 48px;
    letter-spacing: 1px;
  }
  .band {
    position: absolute;
    left: 0;
    right: 0;
    bottom: 0;
    background: var(--taupe);
    color: var(--text-light);
  }
  .band--tagline {
    height: 86px;
    text-align: center;
    font-size: 24px;
    padding-top: 12px;
    letter-spacing: 0.2px;
  }
  .photo {
    position: absolute;
    left: 0;
    top: 0;
    width: 816px;
    height: 438px;
    background: linear-gradient(160deg, var(--teal-light) 0%, var(--teal) 55%, var(--teal-deep) 100%);
  }
  .photo-rule {
    position: absolute;
    left: 0;
    right: 0;
    top: 438px;
    height: 3px;
    background: var(--card-white);
  }
  .band--web {
    height: 86px;
    text-align: right;
    padding: 14px 54px 0 0;
    font-size: 24px;
  }
  .contact {
    position: absolute;
    left: 56px;
    top: 240px;
    color: var(--text-light);
  }
  .contact__name { font-size: 37px; line-height: 44px; }
  .contact__role { font-size: 23px; line-height: 28px; margin-bottom: 20px; }
  .contact__line {
    display: flex;
    align-items: center;
    font-size: 24px;
    line-height: 34px;
  }
  .contact__icon {
    width: 26px;
    height: 26px;
    border-radius: 50%;
    background: var(--card-white);
    color: var(--teal);
    font-size: 16px;
    font-weight: 400;
    display: inline-flex;
    align-items: center;
    justify-content: center;
    margin-right: 10px;
  }
</style>
</head>
<body>
  <section class="card card--front">
    <div class="business-name">Mabel’s Fitness</div>
    <div class="band band--tagline">Become your happiest, healthiest and strongest self</div>
  </section>

  <section class="card card--back">
    <div class="photo" role="img" aria-label="Teal-toned photo of a woman and a trainer doing plank exercises on a gym mat"></div>
    <div class="photo-rule"></div>
    <div class="contact">
      <div class="contact__name">Mabel Quint Harlow</div>
      <div class="contact__role">Personal Trainer</div>
      <div class="contact__line"><span class="contact__icon">t</span>07815 30462</div>
      <div class="contact__line"><span class="contact__icon">e</span>mabel@mabelsfitstudio.example</div>
    </div>
    <div class="band band--web">www.mabelsfitstudio.example</div>
  </section>
</body>
</html>
```